Business Card for Lia Margot Fennick - Psychotherapist specializing in work with youth

I need a simple, elegant, and modern looking business card for my psychotherapy practice. Information on the card that I want is as follows:

Lia Margot Fennick, LMFT
Psychotherapy for Children and Adolescents
415-738-2216
lia.fennick@quillpost.com
418 Tanager Street
Mill Valley, CA 94941
www.liafennick.com
I'd like to create a small image/logo for the card. Something simple, elegant, and modern. Maybe a simple circle? The colors I'm hoping to use will match my website:

liafennick.com

Sage green, light gray, and white. Again, something clean. Here are some examples of other designs that I like. But with my colors.

Thanks!!!!!

Target Market(s)

Bay Area culture - I like the modern trends of using lots of clean looking white, fonts that have an old fashioned, yet modernized edge.

My target is teenagers, but mostly they hear about me through their parents. So something professional looking.

Industry/Entity Type

Business

Contact Information for Business Card

415-738-2216
lia.fennick@quillpost.com

418 Tanager Street
Mill Valley, CA 94941

www.liafennick.com

LICENSED MARRIAGE AND FAMILY THERAPIST #MFC37264 (this last bit of information should only be included if it fits on the card without messing up the design. If we do include - please make this part TINY and towards the bottom of the card)

Font styles to use
Serif

Colors
cadf82
ffffff
dbdbdb

Requirements
Must have
• My information with a nice layout. A simple logo. Great font. The colors I listed:
• sage green, light grey, and white (probably a white card?) See my website for specific color scheme idea:
• liafennick.com
Nice to have
• I'm open to printing the card on nice paper - a thick raw white for example? This can be part of the design?
• I'm also open to a double sided card? I just selected single as it's easier perhaps?

```html
<!DOCTYPE html>
<html lang="en">
<head>
<meta charset="utf-8">
<title>Lia Margot Fennick — Business Card</title>
<link rel="stylesheet" href="https://fonts.googleapis.com/css2?family=Libre+Baskerville:wght@400;700&family=Open+Sans:wght@400&display=swap">
<style>
  :root {
    --paper: #ffffff;
    --canvas-bg: #ffffff;
    --card-edge: #c9d3ad;
    --sage-text: #97ad5b;
    --dot-rule: #b9cc7e;
    --ink: #2f3324;
    --sage-light: #cadf82;
    --sage-mid: #b5cc6e;
    --sage-deep: #9fb85c;
    --bloom-light: #e4edc2;
    --bloom-mid: #b9cf78;
    --contact-text: #ffffff;
  }
  * { box-sizing: border-box; margin: 0; padding: 0; }
  html, body {
    width: 696px;
    height: 1200px;
    overflow: hidden;
    background: var(--canvas-bg);
  }
  .card {
    position: absolute;
    left: 28px;
    top: 23px;
    width: 640px;
    height: 1148px;
    border: 2px solid var(--card-edge);
    border-radius: 42px;
    overflow: hidden;
    background: var(--paper);
  }
  .card-header {
    position: absolute;
    left: 0; top: 0;
    width: 100%;
    height: 380px;
    text-align: center;
  }
  .practitioner-name {
    position: absolute;
    top: 52px;
    width: 100%;
    font-family: "Libre Baskerville", Georgia, serif;
    font-weight: 700;
    font-size: 44px;
    letter-spacing: -0.5px;
    color: var(--sage-text);
  }
  .dotted-rule {
    position: absolute;
    left: 38px;
    right: 38px;
    top: 126px;
    border-top: 4px dotted var(--dot-rule);
  }
  .practice-tagline {
    position: absolute;
    top: 162px;
    width: 100%;
    font-family: "Libre Baskerville", Georgia, serif;
    font-size: 21px;
    color: var(--ink);
  }
  .card-body {
    position: absolute;
    left: 0; top: 380px;
    width: 100%;
    height: 768px;
    background: radial-gradient(ellipse 70% 45% at 50% 42%, var(--sage-light) 0%, var(--sage-mid) 65%, var(--sage-deep) 100%);
  }
  .bloom-art {
    position: absolute;
    left: 160px;
    top: 205px;
    width: 320px;
    height: 320px;
    border-radius: 50%;
    background: radial-gradient(circle, var(--paper) 0%, var(--bloom-light) 22%, var(--bloom-mid) 58%, rgba(185,207,120,0) 72%);
  }
  .contact {
    position: absolute;
    left: 58px;
    font-family: "Open Sans", Arial, sans-serif;
    font-size: 40px;
    line-height: 1.45;
    color: var(--contact-text);
    text-shadow: 0 2px 4px rgba(60, 75, 30, 0.45);
  }
  .contact-phone { top: 625px; }
  .contact-web { top: 800px; }
  .contact-address { top: 945px; }
</style>
</head>
<body>
  <main class="card">
    <header class="card-header">
      <h1 class="practitioner-name">Lia Margot Fennick</h1>
      <div class="dotted-rule"></div>
      <p class="practice-tagline">Psychotherapy for Children and Adolescents</p>
    </header>
    <section class="card-body"></section>
    <div class="bloom-art" role="img" aria-label="Pale sage green flower illustration"></div>
    <p class="contact contact-phone">Tel : 415-738-2216</p>
    <p class="contact contact-web">Web : liafennick.com</p>
    <address class="contact contact-address" style="font-style:normal">418 Tanager Street<br>Mill Valley, CA 94941</address>
  </main>
</body>
</html>
```